Social Health & Parkinson's

I need a 1-pg horizontal infographic that can be handed out to patients and providers. It needs to be scientifically sound (data provided), easy to understand, and visually pleasing. Target audience; patiens (mostly 40-90 years old) and providers (neurologists, nurses, physical therapists, naturopathic physicians, support group leaders, etc.) We need 6 of these, one for each topic listed on the website. Ideally, we'll hire the winner for 5 more similar projects and keep a theme.

Target Market(s)

Patients with Parkinson's disease, their families, care providers. To be handed out by physicians, support group leaders, etc.

Colors

Designer to choose colors to be used in the design.

Requirements
Must have
• Visually stunning. Data integrity-- keep the numbers and the figures we provide. Reference to where the data is coming from. Be thoughtful of elderly, vision issues. Teach everyone something.

```html
<!DOCTYPE html>
<html lang="en">
<head>
<meta charset="utf-8">
<title>Social Health &amp; Patient-Reported Outcomes in PD</title>
<link rel="stylesheet" href="https://fonts.googleapis.com/css2?family=Bebas+Neue&family=Barlow:wght@400;500;600;700&display=swap">
<style>
  :root {
    --navy: #223f8e;
    --blue: #2a4c9f;
    --orange: #e07030;
    --orange-mid: #f08848;
    --orange-light: #f9a26e;
    --orange-pale: #fdbd97;
    --panel-grey: #e6e6e6;
    --text-dark: #1d1d1d;
    --divider: #e2e2e2;
    --white: #ffffff;
  }
  * { margin: 0; padding: 0; box-sizing: border-box; }
  html, body { width: 1200px; height: 936px; overflow: hidden; background: var(--white); }
  body { font-family: "Barlow", sans-serif; color: var(--text-dark); }
  .infographic { position: relative; width: 1200px; height: 936px; overflow: hidden; background: var(--white); }

  .band-top { position: absolute; left: 0; top: 31px; width: 1200px; height: 19px; background: var(--navy); }
  .band-orange { position: absolute; left: 0; top: 50px; width: 1200px; height: 27px; background: var(--orange); }
  .header-left { position: absolute; left: 0; top: 77px; width: 272px; height: 96px; background: var(--navy); border-bottom-right-radius: 48px; }
  .header-title-block { position: absolute; left: 299px; top: 77px; width: 901px; height: 96px; background: var(--blue); border-top-left-radius: 30px; border-bottom-left-radius: 40px; }

  .tagline { position: absolute; left: 355px; top: 52px; height: 24px; line-height: 24px; color: var(--white); font-weight: 500; font-size: 17px; letter-spacing: 2.2px; white-space: nowrap; }
  .main-title { position: absolute; left: 350px; top: 98px; font-family: "Bebas Neue", sans-serif; font-weight: 400; font-size: 47px; line-height: 52px; color: var(--white); white-space: nowrap; letter-spacing: 0.3px; }

  .partner { position: absolute; left: 30px; display: flex; align-items: center; gap: 9px; color: var(--white); font-weight: 600; font-size: 14px; }
  .partner-dot { width: 14px; height: 14px; border-radius: 50%; background: var(--white); }
  .partner-one { top: 100px; }
  .partner-two { top: 132px; }

  .column-divider { position: absolute; top: 173px; width: 1px; height: 717px; background: var(--divider); }

  .callout { position: absolute; background: var(--panel-grey); font-size: 13.4px; line-height: 17px; text-align: justify; }
  .callout p + p { margin-top: 17px; }
  .callout-scores { left: 0; top: 440px; width: 354px; height: 48px; border-radius: 0 26px 26px 0; padding: 6px 20px 0 21px; font-size: 16px; line-height: 18px; text-align: left; font-weight: 500; }
  .callout-loneliness { left: 394px; top: 497px; width: 442px; height: 127px; border-radius: 14px; padding: 8px 10px 0 11px; }
  .callout-summary { left: 874px; top: 497px; width: 326px; height: 141px; border-radius: 14px 0 0 14px; padding: 8px 20px 0 12px; }

  .care-illustration { position: absolute; left: 896px; top: 664px; width: 246px; height: 158px; border-radius: 60px 60px 20px 20px; background: linear-gradient(180deg, #2b4aa0 0%, #203a84 100%); }

  .footer { position: absolute; left: 0; top: 822px; width: 1200px; height: 114px; background: var(--navy); border-radius: 46px 46px 0 0; display: flex; align-items: center; justify-content: center; color: var(--white); font-size: 16px; font-weight: 600; letter-spacing: 2.4px; }

  .charts { position: absolute; left: 0; top: 0; width: 1200px; height: 936px; font-family: "Barlow", sans-serif; }
  .chart-title { fill: var(--blue); font-weight: 600; font-size: 12px; text-anchor: middle; }
  .axis-label { fill: var(--text-dark); font-size: 7.5px; font-weight: 600; }
  .tick { fill: var(--text-dark); font-size: 7.5px; font-weight: 600; }
  .tiny { fill: var(--text-dark); font-size: 5.5px; font-weight: 500; }
  .side-tag-text { fill: var(--white); font-weight: 700; font-size: 10px; letter-spacing: 1px; }
  .grid { stroke: #d9d9d9; stroke-width: 0.8; }
  .grid-orange { stroke: #f3946a; stroke-width: 0.7; }
</style>
</head>
<body>
<main class="infographic">

  <div class="band-top"></div>
  <div class="band-orange"></div>
  <div class="header-left"></div>
  <div class="header-title-block"></div>

  <svg class="charts" viewBox="0 0 1200 936" aria-hidden="false">
    <!-- header arrow and flag -->
    <polygon points="285,37 316,77 299,77 299,173 272,173 272,77 256,77" fill="var(--white)"/>
    <line x1="285" y1="9" x2="285" y2="37" stroke="#777" stroke-width="1.2"/>
    <rect x="286" y="8" width="18" height="11" fill="var(--orange)"/>

    <!-- ===== Correlation chart ===== -->
    <text class="chart-title" x="232" y="254">Correlation Between</text>
    <text class="chart-title" x="232" y="268">Quality of Life and PRO-PD Score</text>
    <rect x="22" y="274" width="19" height="130" fill="var(--navy)"/>
    <text class="side-tag-text" transform="translate(35,339) rotate(-90)" text-anchor="middle">PRO-PD Score</text>
    <g>
      <rect x="110" y="274" width="179" height="51" fill="var(--orange-pale)"/>
      <rect x="110" y="325" width="179" height="26" fill="var(--orange-light)"/>
      <rect x="110" y="351" width="179" height="26" fill="var(--orange-mid)"/>
      <rect x="110" y="377" width="179" height="27" fill="var(--orange)"/>
      <rect x="307" y="274" width="46" height="51" fill="var(--orange-pale)"/>
      <rect x="307" y="325" width="46" height="26" fill="var(--orange-light)"/>
      <rect x="307" y="351" width="46" height="26" fill="var(--orange-mid)"/>
      <rect x="307" y="377" width="46" height="27" fill="var(--orange)"/>
      <line x1="110" y1="371" x2="319" y2="314" stroke="#111" stroke-width="0.9"/>
      <g class="tick" text-anchor="end">
        <text x="105" y="279">2500</text><text x="105" y="304">2000</text>
        <text x="105" y="330">1500</text><text x="105" y="355">1000</text>
        <text x="105" y="380">500</text><text x="105" y="405">0</text>
      </g>
      <g class="tick" text-anchor="middle">
        <text x="146" y="414">5</text><text x="181" y="414">10</text><text x="215" y="414">15</text>
        <text x="249" y="414">20</text><text x="284" y="414">25</text><text x="319" y="414">30</text><text x="353" y="414">35</text>
      </g>
      <text class="axis-label" x="231" y="427" text-anchor="middle">Years Since Diagnosis</text>
      <text transform="translate(301,339) rotate(-90)" text-anchor="middle" fill="var(--blue)" font-weight="700" font-size="10" letter-spacing="1">Quality of Life</text>
      <g class="tick" text-anchor="middle" font-size="8.5">
        <text x="330" y="305">Poor</text><text x="330" y="341">*Fair</text>
        <text x="330" y="367">Good</text><text x="330" y="393">Excellent</text>
      </g>
    </g>

    <!-- ===== Satisfaction bar chart ===== -->
    <text class="chart-title" x="202" y="515" font-size="9.5">In general, please rate how well you rate your satisfaction with</text>
    <text class="chart-title" x="202" y="526" font-size="9.5">your social activities and relationships</text>
    <rect x="22" y="537" width="19" height="76" fill="var(--navy)"/>
    <text class="side-tag-text" transform="translate(35,575) rotate(-90)" text-anchor="middle">PRO-PD</text>
    <g class="tick" text-anchor="end" font-size="7">
      <text x="116" y="546">2000</text><text x="116" y="563">1500</text><text x="116" y="581">1000</text>
      <text x="116" y="598">500</text><text x="116" y="616">0</text>
    </g>
    <line x1="125" y1="540" x2="125" y2="613" stroke="#999" stroke-width="0.7"/>
    <line x1="125" y1="613" x2="345" y2="613" stroke="#999" stroke-width="0.7"/>
    <polygon points="350,613 343,610 343,616" fill="#999"/>
    <rect x="142" y="595.5" width="20" height="17.5" fill="#fde0d0"/>
    <rect x="183" y="589" width="20" height="24" fill="#fbc7a6"/>
    <rect x="224" y="581" width="20" height="32" fill="#f8a478"/>
    <rect x="265" y="571" width="20" height="42" fill="#f38a4f"/>
    <rect x="306" y="566" width="20" height="47" fill="var(--orange)"/>
    <g class="tiny" text-anchor="middle">
      <text x="152" y="592">494</text><text x="193" y="586">667</text><text x="234" y="578">889</text>
      <text x="275" y="568">1178</text><text x="316" y="563">1317</text>
      <text x="152" y="621">Excellent</text><text x="193" y="621">Very Good</text><text x="234" y="621">Good</text>
      <text x="275" y="621">Fair</text><text x="316" y="621">Poor</text>
      <text x="152" y="628">(n=343)</text><text x="193" y="628">(n=607)</text><text x="234" y="628">(n=468)</text>
      <text x="275" y="628">(n=268)</text><text x="316" y="628">(n=61)</text>
      <text x="234" y="643" font-size="6">Social Satisfaction</text>
    </g>

    <!-- ===== Roles bar chart ===== -->
    <text class="chart-title" x="202" y="676" font-size="9.5">In general, please rate how well you carry out</text>
    <text class="chart-title" x="202" y="687" font-size="9.5">your social activities and roles</text>
    <rect x="22" y="697" width="19" height="76" fill="var(--navy)"/>
    <text class="side-tag-text" transform="translate(35,735) rotate(-90)" text-anchor="middle">PRO-PD</text>
    <g class="tick" text-anchor="end" font-size="7">
      <text x="116" y="706">2000</text><text x="116" y="724">1500</text><text x="116" y="741">1000</text>
      <text x="116" y="758">500</text><text x="116" y="776">0</text>
    </g>
    <line x1="125" y1="700" x2="125" y2="773" stroke="#999" stroke-width="0.7"/>
    <line x1="125" y1="773" x2="345" y2="773" stroke="#999" stroke-width="0.7"/>
    <polygon points="350,773 343,770 343,776" fill="#999"/>
    <rect x="142" y="757" width="20" height="16" fill="#fde0d0"/>
    <rect x="183" y="750" width="20" height="23" fill="#fbc7a6"/>
    <rect x="224" y="738" width="20" height="35" fill="#f8a478"/>
    <rect x="265" y="729" width="20" height="44" fill="#f38a4f"/>
    <rect x="306" y="721" width="20" height="52" fill="var(--orange)"/>
    <g class="tiny" text-anchor="middle">
      <text x="152" y="754">446</text><text x="193" y="747">653</text><text x="234" y="735">992</text>
      <text x="275" y="726">1233</text><text x="316" y="718">1464</text>
      <text x="152" y="781">Excellent</text><text x="193" y="781">Very Good</text><text x="234" y="781">Good</text>
      <text x="275" y="781">Fair</text><text x="316" y="781">Poor</text>
      <text x="152" y="788">(n=322)</text><text x="193" y="788">(n=647)</text><text x="234" y="788">(n=491)</text>
      <text x="275" y="788">(n=247)</text><text x="316" y="788">(n=44)</text>
      <text x="234" y="802" font-size="6">Social Satisfaction</text>
    </g>

    <!-- ===== Modifiable variables chart ===== -->
    <text class="chart-title" x="638" y="254">Modifiable variables associated with</text>
    <text class="chart-title" x="638" y="268">risk of parkinsons disease</text>
    <g class="grid">
      <line x1="512" y1="276" x2="512" y2="454"/><line x1="555" y1="276" x2="555" y2="454"/>
      <line x1="598" y1="276" x2="598" y2="454"/><line x1="640" y1="276" x2="640" y2="454"/>
      <line x1="683" y1="276" x2="683" y2="454"/><line x1="712" y1="276" x2="712" y2="454"/>
      <line x1="750" y1="276" x2="750" y2="454"/><line x1="789" y1="276" x2="789" y2="454"/>
      <line x1="828" y1="276" x2="828" y2="454"/>
    </g>
    <g fill="#ea7c3c">
      <rect x="555" y="280" width="122" height="6"/>
      <rect x="561" y="297" width="116" height="6"/>
      <rect x="581" y="313" width="96" height="6"/>
      <rect x="587" y="330" width="90" height="6"/>
      <rect x="604" y="346" width="73" height="6"/>
      <rect x="612" y="363" width="65" height="6"/>
      <rect x="621" y="379" width="56" height="6"/>
      <rect x="661" y="395" width="16" height="6"/>
      <rect x="677" y="412" width="63" height="6"/>
      <rect x="677" y="427" width="69" height="6"/>
      <rect x="677" y="443" width="139" height="6"/>
    </g>
    <g class="tick" font-size="7">
      <text x="402" y="286">Exercise 30+ min/d, 7 days/wk</text>
      <text x="402" y="302">Exercise 30+ min/d, 6 days/wk</text>
      <text x="402" y="319">Exercise 30+ min/d, 5 days/wk</text>
      <text x="402" y="335">Exercise 30+ min/d, 4 days/wk</text>
      <text x="402" y="352">Exercise 30+ min/d, 3 days/wk</text>
      <text x="402" y="368">I have lots of friends</text>
      <text x="402" y="385">I cook most of my meals</text>
      <text x="402" y="401">I practice stress management</text>
      <text x="402" y="418">I am overweight</text>
      <text x="402" y="434">I have a lot of stress</text>
      <text x="402" y="450">I am lonely</text>
    </g>
    <g class="tiny">
      <text x="681" y="286">-301</text><text x="681" y="302">-292</text><text x="681" y="319">-237</text>
      <text x="681" y="335">-229</text><text x="681" y="352">-192</text><text x="681" y="368">-168</text>
      <text x="681" y="385">-146</text><text x="681" y="400">-46</text>
      <text x="671" y="418" text-anchor="end">139</text><text x="671" y="433" text-anchor="end">180</text>
      <text x="671" y="449" text-anchor="end">328</text>
    </g>
    <g class="tick" text-anchor="middle" font-size="7">
      <text x="512" y="467">-400</text><text x="555" y="467">-300</text><text x="598" y="467">-200</text>
      <text x="640" y="467">-100</text><text x="677" y="467">0</text><text x="712" y="467">100</text>
      <text x="750" y="467">200</text><text x="789" y="467">300</text><text x="828" y="467">400</text>
    </g>

    <!-- ===== Quality of Life vs Tremor ===== -->
    <text class="chart-title" x="518" y="660">Quality of Life vs. Tremor</text>
    <rect x="393" y="667" width="16" height="122" fill="var(--navy)"/>
    <text transform="translate(404,728) rotate(-90)" text-anchor="middle" fill="var(--white)" font-weight="600" font-size="7">PROMIS Total-Quality of Life</text>
    <rect x="430" y="673" width="174" height="108" fill="none" class="grid-orange"/>
    <g class="grid-orange">
      <line x1="465" y1="673" x2="465" y2="781"/><line x1="500" y1="673" x2="500" y2="781"/>
      <line x1="534" y1="673" x2="534" y2="781"/><line x1="569" y1="673" x2="569" y2="781"/>
      <line x1="430" y1="691" x2="604" y2="691"/><line x1="430" y1="709" x2="604" y2="709"/>
      <line x1="430" y1="727" x2="604" y2="727"/><line x1="430" y1="745" x2="604" y2="745"/>
      <line x1="430" y1="763" x2="604" y2="763"/>
    </g>
    <line x1="430" y1="709" x2="604" y2="727" stroke="var(--navy)" stroke-width="2" stroke-dasharray="2 2.4"/>
    <text class="tiny" x="599" y="685" text-anchor="end">R² = 0.0754</text>
    <g class="tick" text-anchor="end" font-size="7">
      <text x="424" y="676">60</text><text x="424" y="694">50</text><text x="424" y="712">40</text>
      <text x="424" y="730">30</text><text x="424" y="748">20</text><text x="424" y="766">10</text><text x="424" y="784">0</text>
    </g>
    <g class="tick" text-anchor="middle" font-size="7">
      <text x="432" y="793">0</text><text x="466" y="793">20</text><text x="500" y="793">40</text>
      <text x="534" y="793">60</text><text x="569" y="793">80</text><text x="602" y="793">100</text>
    </g>
    <text class="axis-label" x="518" y="805" text-anchor="middle">Tremor</text>

    <!-- ===== Quality of Life vs Withdrawn ===== -->
    <text class="chart-title" x="747" y="660">Quality of Life vs. Withdrawn</text>
    <rect x="623" y="667" width="16" height="122" fill="var(--navy)"/>
    <text transform="translate(634,728) rotate(-90)" text-anchor="middle" fill="var(--white)" font-weight="600" font-size="7">PROMIS Total-Quality of Life</text>
    <rect x="660" y="673" width="174" height="108" fill="none" class="grid-orange"/>
    <g class="grid-orange">
      <line x1="695" y1="673" x2="695" y2="781"/><line x1="730" y1="673" x2="730" y2="781"/>
      <line x1="764" y1="673" x2="764" y2="781"/><line x1="799" y1="673" x2="799" y2="781"/>
      <line x1="660" y1="691" x2="834" y2="691"/><line x1="660" y1="709" x2="834" y2="709"/>
      <line x1="660" y1="727" x2="834" y2="727"/><line x1="660" y1="745" x2="834" y2="745"/>
      <line x1="660" y1="763" x2="834" y2="763"/>
    </g>
    <line x1="660" y1="709" x2="834" y2="745" stroke="var(--navy)" stroke-width="2" stroke-dasharray="2 2.4"/>
    <text class="tiny" x="829" y="685" text-anchor="end">R² = 0.4872</text>
    <g class="tick" text-anchor="end" font-size="7">
      <text x="654" y="676">60</text><text x="654" y="694">50</text><text x="654" y="712">40</text>
      <text x="654" y="730">30</text><text x="654" y="748">20</text><text x="654" y="766">10</text><text x="654" y="784">0</text>
    </g>
    <g class="tick" text-anchor="middle" font-size="7">
      <text x="662" y="793">0</text><text x="696" y="793">20</text><text x="730" y="793">40</text>
      <text x="764" y="793">60</text><text x="799" y="793">80</text><text x="832" y="793">100</text>
    </g>
    <text class="axis-label" x="755" y="805" text-anchor="middle">Withdrawn</text>

    <!-- ===== Average PRO-PD line chart ===== -->
    <text class="chart-title" x="1006" y="255" font-size="11">Average PRO-PD by Years  Since Diganosis</text>
    <rect x="865" y="270" width="18" height="84" fill="var(--navy)"/>
    <text class="side-tag-text" transform="translate(878,312) rotate(-90)" text-anchor="middle">PRO-PD</text>
    <line x1="925" y1="276" x2="925" y2="405" stroke="#999" stroke-width="0.7"/>
    <line x1="925" y1="405" x2="1133" y2="405" stroke="#999" stroke-width="0.7"/>
    <polygon points="1139,405 1132,402 1132,408" fill="#999"/>
    <g class="tick" text-anchor="end" font-size="7">
      <text x="918" y="283">1400</text><text x="918" y="301">1200</text><text x="918" y="318">1000</text>
      <text x="918" y="336">800</text><text x="918" y="353">600</text><text x="918" y="371">400</text>
      <text x="918" y="388">200</text><text x="918" y="407">0</text>
    </g>
    <g class="tiny" text-anchor="middle">
      <text x="933" y="415">0</text><text x="952" y="415">1</text><text x="970" y="415">2</text>
      <text x="988" y="415">3</text><text x="1007" y="415">4</text><text x="1025" y="415">5</text>
      <text x="1044" y="415">6</text><text x="1062" y="415">7</text><text x="1080" y="415">8</text>
      <text x="1099" y="415">9</text><text x="1117" y="415">10</text>
      <text x="1034" y="427">Years Since Diagnosis</text>
    </g>
    <polyline fill="none" stroke="#f08a4b" stroke-width="1" points="933,320 952,328 970,321 988,324 1007,313 1025,302 1044,291 1062,302 1080,314 1099,290 1117,289"/>
    <g fill="#f08a4b">
      <circle cx="933" cy="320" r="1.8"/><circle cx="952" cy="328" r="1.8"/><circle cx="970" cy="321" r="1.8"/>
      <circle cx="988" cy="324" r="1.8"/><circle cx="1007" cy="313" r="1.8"/><circle cx="1025" cy="302" r="1.8"/>
      <circle cx="1044" cy="291" r="1.8"/><circle cx="1062" cy="302" r="1.8"/><circle cx="1080" cy="314" r="1.8"/>
      <circle cx="1099" cy="290" r="1.8"/><circle cx="1117" cy="289" r="1.8"/>
    </g>
    <polyline fill="none" stroke="var(--blue)" stroke-width="1" points="933,358 952,351 970,352 988,345 1007,348 1025,344 1044,334 1062,329 1080,326 1099,321 1117,319"/>
    <g fill="var(--blue)">
      <circle cx="933" cy="358" r="1.8"/><circle cx="952" cy="351" r="1.8"/><circle cx="970" cy="352" r="1.8"/>
      <circle cx="988" cy="345" r="1.8"/><circle cx="1007" cy="348" r="1.8"/><circle cx="1025" cy="344" r="1.8"/>
      <circle cx="1044" cy="334" r="1.8"/><circle cx="1062" cy="329" r="1.8"/><circle cx="1080" cy="326" r="1.8"/>
      <circle cx="1099" cy="321" r="1.8"/><circle cx="1117" cy="319" r="1.8"/>
    </g>
    <g class="tiny" font-size="4.5" text-anchor="middle">
      <text x="933" y="315">961</text><text x="952" y="323">881</text><text x="970" y="329">963</text>
      <text x="988" y="319">928</text><text x="1009" y="320">1053</text><text x="1026" y="309">1180</text>
      <text x="1044" y="286">1304</text><text x="1066" y="298">1180</text><text x="1082" y="309">1043</text>
      <text x="1104" y="297">1319</text><text x="1125" y="288">1330</text>
      <text x="933" y="365">539</text><text x="952" y="347">616</text><text x="970" y="359">603</text>
      <text x="988" y="341">681</text><text x="1007" y="355">648</text><text x="1026" y="351">691</text>
      <text x="1046" y="340">808</text><text x="1064" y="335">858</text><text x="1082" y="332">895</text>
      <text x="1101" y="327">947</text><text x="1125" y="320">975</text>
    </g>
    <rect x="965" y="433" width="129" height="22" fill="none" stroke="#aaa" stroke-width="0.6" stroke-dasharray="2 2"/>
    <line x1="975" y1="444" x2="995" y2="444" stroke="#f08a4b" stroke-width="1"/>
    <circle cx="985" cy="444" r="2" fill="#f08a4b"/>
    <text class="tiny" x="998" y="446" font-size="5.5">LONELY</text>
    <line x1="1025" y1="444" x2="1045" y2="444" stroke="var(--blue)" stroke-width="1"/>
    <circle cx="1035" cy="444" r="2" fill="var(--blue)"/>
    <text class="tiny" x="1048" y="446" font-size="5.5">NOT LONELY</text>
  </svg>

  <p class="tagline">Rx: Nurture social health &nbsp;●&nbsp; Make friends &nbsp;●&nbsp; Avoid loneliness.</p>
  <h1 class="main-title">SOCIAL HEALTH &amp; PATIENT - REPORTED OUTCOMES IN PD</h1>

  <div class="partner partner-one"><span class="partner-dot"></span><span>Northgate University</span></div>
  <div class="partner partner-two"><span class="partner-dot"></span><span>Steady Steps</span></div>

  <div class="column-divider" style="left:376px"></div>
  <div class="column-divider" style="left:854px"></div>

  <div class="callout callout-scores">PRO-PD scores increased as measures of social health worsend</div>

  <div class="callout callout-loneliness">
    <p>Individuals who reported feeling lonely reported greater overall PD symptom severity (+328; p=0.000), which was even higher than scores for smoking tobacco (+180; p=0.000).</p>
    <p>In contrast individuals that reported having a lot of friends had reduced PD severity scores (-168; p=0.000). Notably, exercising 7 days per week was less beneficial (-301; p=0.000) than feeling lonely was detrimental.</p>
  </div>

  <div class="callout callout-summary">
    <p>Overall, individuals identifying as being lonely reported consistently greater PD symptom severity.</p>
    <p>Although tremor is a cardinal symptom of PD and highly visible, feeling socially with-drawn is more closely correlated to overall quality of life than tremor.</p>
  </div>

  <div class="care-illustration" role="img" aria-label="Illustration of two open hands holding a heart with a heartbeat line"></div>

  <footer class="footer">www.WellAheadWithPD.org &nbsp;|&nbsp; 2020 R. Halvorsen</footer>
</main>
</body>
</html>
```